Redesign of Plastic Surgeon Website to fully responsive / modern feel

Hi

Our current website is out of date www.harbourlinecosmetic.org

We want a fresh / modern looking design
Needs to be fully responsive design that works extremely well on ipad and mobile device

Would like design for both full screen website and mobile

Have listed a few websites of other plastic surgeons we like
http://www.reformclinicdaily.com/
http://www.peterholtbymd.com/
http://www.corvanbeauty.com/
http://www.tidewellcontouring.com/

Menu needs to include
1. About Us
2. Procedures (see current website for example)
3. News
4. Patient Resources
5. Contact Us

We are flexible with colours / images / layout

I have uploaded a document that has some content - the face pages content is completed only

some of the procedures can have content upwards of 4000 words - total website can be large with over 40,000 words
Updates

Target Market(s)

Mainly women 20-60 85% of practice
Some men 15%

Industry/Entity Type

Plastic Surgery

Number of Pages Required

5+ page

Requirements
Must have
• We need designs for
• Homepage
• Internal pages
• 1. Landing pages for breast / body / face / non surgical main pages
• 2. Procedure pages for individual pages under each section - eg breast augmentation
• 3. About us pages - like meet the doctor, our staff, clinics
• 4. Contact page
• 5. Blog / News page
Nice to have
• See our list of websites for examples of designs we like
• Like full screen design with nice hero image
• Needs to have good to call to action messages on home page like
• Specials, procedure of the month, etc

```html
<!DOCTYPE html>
<html lang="en">
<head>
<meta charset="utf-8">
<title>Harbourline Institute of Plastic Surgery</title>
<link rel="stylesheet" href="https://fonts.googleapis.com/css2?family=Raleway:wght@300;400;500;600;700&family=Open+Sans:wght@400;600&display=swap">
<style>
:root{
  --copper:#d4a06a;
  --copper-dark:#b7834f;
  --copper-band:#b9824c;
  --dark:#3b3734;
  --darker:#2d2a28;
  --footer:#262321;
  --ink:#3a3a3a;
  --muted:#777;
  --light:#f1f1f1;
  --white:#fff;
}
*{box-sizing:border-box;margin:0;padding:0}
html,body{width:1200px;height:4545px;overflow:hidden}
body{font-family:"Open Sans",Arial,sans-serif;color:var(--ink);background:var(--white);position:relative}
section,header,footer{position:relative;width:1200px;overflow:hidden}
.abs{position:absolute}
.h-title{font-family:"Raleway",Arial,sans-serif;font-weight:500;text-transform:uppercase;letter-spacing:1px}
.btn{display:inline-block;font-family:"Raleway",Arial,sans-serif;font-size:11px;font-weight:700;text-transform:uppercase;letter-spacing:.5px;padding:0 18px;height:32px;line-height:32px;border-radius:2px;white-space:nowrap}
.btn-copper{background:var(--copper);color:var(--white)}
.btn-white{background:var(--white);color:var(--ink)}
.btn-dark{background:var(--dark);color:var(--white)}
.ornament{position:absolute;left:50%;transform:translateX(-50%);width:70px;height:14px}
.center{text-align:center;left:0;right:0}

/* header */
.site-header{height:121px;background:var(--white)}
.brand{left:210px;top:14px;display:flex;align-items:center;gap:10px}
.brand-mark{width:38px;height:38px;border:2px solid var(--copper)}
.brand-name{font-family:"Raleway",Arial,sans-serif;font-size:28px;font-weight:400;color:#555;line-height:1}
.request{right:210px;top:12px;font-family:"Raleway",Arial,sans-serif;font-size:17px;color:#666}
.request b{color:var(--copper);font-weight:600}
.header-btns{right:210px;top:42px;display:flex;gap:8px}
.header-btns .btn{height:28px;line-height:28px;font-size:10px}
.main-nav{right:210px;top:94px;display:flex;gap:22px;font-family:"Raleway",Arial,sans-serif;font-size:11px;font-weight:600;text-transform:uppercase;color:#555}
.main-nav .active{color:var(--copper)}

/* hero */
.hero{height:400px;background:linear-gradient(90deg,#ececec,#f6f6f6 55%,#e6e6e6)}
.hero-photo{right:0;top:0;width:620px;height:400px;background:radial-gradient(ellipse at 55% 45%,#f0d4c0 0%,#e2bda4 35%,#d8c1ae 60%,rgba(230,230,230,0) 80%)}
.hero-copy{left:150px;width:500px;top:80px;text-align:center}
.hero-copy h1{font-family:"Raleway",Arial,sans-serif;font-weight:500;font-size:30px;line-height:38px;color:#3a3a3a;text-transform:uppercase;letter-spacing:1px}
.hero-tag{display:flex;align-items:center;justify-content:center;gap:12px;margin-top:12px;font-family:"Raleway",Arial,sans-serif;font-size:14px;letter-spacing:2px;color:#444;text-transform:uppercase}
.hero-tag span.line{width:60px;height:2px;background:var(--copper)}
.play{width:36px;height:36px;margin:22px auto 6px}
.hero-copy p{font-family:"Raleway",Arial,sans-serif;font-style:italic;font-size:15px;color:#444;line-height:20px}
.hero-copy .btn{margin-top:22px}

/* welcome */
.welcome{height:367px;background:var(--white)}
.welcome h2{top:56px;font-size:22px;color:#444}
.welcome .ornament{top:94px}
.welcome .copy{left:210px;width:780px;top:124px;text-align:center;font-size:12px;line-height:20px;color:var(--muted)}
.welcome .copy p+p{margin-top:14px}
.welcome .btn{left:544px;top:270px}

/* procedures */
.procedures{height:506px;background:var(--dark)}
.procedures h2{top:48px;font-size:21px;color:var(--white)}
.procedures .ornament{top:92px}
.proc-item{top:150px;width:200px;text-align:center}
.proc-circle{width:190px;height:190px;margin:0 auto;border-radius:50%;border:3px solid var(--copper);padding:6px;background:var(--dark)}
.proc-circle div{width:100%;height:100%;border-radius:50%}
.proc-item h3{margin-top:18px;font-family:"Raleway",Arial,sans-serif;font-size:15px;font-weight:600;color:var(--white)}
.proc-btns{left:0;right:0;top:414px;display:flex;justify-content:center;gap:10px}

/* doctor */
.doctor{height:509px;background:linear-gradient(90deg,#f4f4f4,#e8e8e8 60%,#dcdcdc)}
.doctor-photo{left:180px;top:0;width:340px;height:509px;background:linear-gradient(180deg,#d7d7d7 0%,#bfc3c8 45%,#8c96a2 80%,#6f7886 100%)}
.doctor-copy{left:538px;top:36px;width:460px}
.doctor-copy h2{font-family:"Raleway",Arial,sans-serif;font-size:22px;font-weight:500;color:#444;text-transform:uppercase}
.doctor-copy .intro{margin-top:14px;font-size:12px;line-height:19px;color:var(--muted)}
.doctor-copy h3{margin-top:22px;font-family:"Raleway",Arial,sans-serif;font-size:20px;font-weight:500;color:#444;text-transform:uppercase}
.affil{margin-top:14px;list-style:none}
.affil li{display:flex;align-items:center;gap:10px;font-size:11.5px;color:#555;height:23px}
.affil svg{width:12px;height:12px;flex:none}
.doctor-btns{margin-top:22px;display:flex;gap:10px}

/* certified */
.certified{height:182px;background:var(--white)}
.certified h2{left:212px;top:74px;font-size:20px;color:var(--copper)}
.badge{top:55px;width:58px;height:58px;border-radius:50%;border:2px solid #c9ccd4;background:#eef0f4}
.badge.square{border-radius:4px;width:66px;height:40px;top:64px;background:#dfe3ec}

/* features */
.features{height:309px;background:linear-gradient(90deg,#a86f3b,#c38d56 50%,#a86f3b)}
.feature-card{top:12px;width:214px;height:286px;background:var(--white);border:4px solid #f1e6da;text-align:center}
.feature-card .pic{height:120px}
.feature-card h3{margin-top:18px;font-family:"Raleway",Arial,sans-serif;font-size:14px;font-weight:700;color:#444;text-transform:uppercase}
.feature-card p{margin:8px 18px 0;font-size:11px;line-height:16px;color:var(--muted)}
.feature-card .btn{margin-top:14px;height:28px;line-height:28px}

/* gallery */
.gallery{height:621px;background:var(--darker)}
.gallery h2{top:100px;font-size:20px;color:var(--white)}
.gallery .ornament{top:138px}
.tabs{left:378px;top:190px;display:flex;gap:40px;font-family:"Raleway",Arial,sans-serif;font-size:13px;font-weight:600;letter-spacing:2px;color:#ddd}
.tabs span{padding-bottom:6px}
.tabs .on{color:var(--white);border-bottom:2px solid var(--copper)}
.tab-rule{left:378px;top:214px;width:440px;height:1px;background:#555}
.gallery-photo{left:224px;top:212px;width:206px;height:206px;border-radius:50%;border:3px solid var(--copper);padding:8px}
.gallery-photo div{width:100%;height:100%;border-radius:50%;background:radial-gradient(circle at 50% 45%,#f0cdb0,#c79a76 60%,#8a6a4c)}
.gallery-copy{left:521px;top:236px;width:480px}
.gallery-copy h3{font-family:"Raleway",Arial,sans-serif;font-size:20px;font-weight:500;color:var(--white)}
.gallery-copy p{margin-top:12px;font-size:11.5px;line-height:18px;color:#bbb}
.gallery-copy .hint{margin-top:22px;font-size:13px;color:var(--copper)}
.g-list{margin-top:10px;display:grid;grid-template-columns:190px 190px;list-style:none;row-gap:6px}
.g-list li{font-size:11.5px;color:#ddd;display:flex;align-items:center;gap:8px}
.g-list li::before{content:"";width:5px;height:5px;border-radius:50%;background:var(--copper)}
.gallery-btns{margin-top:26px;display:flex;gap:10px}

/* blog & team */
.blog-team{height:506px;background:linear-gradient(180deg,#ececec,#dedede)}
.blog-team h2{top:68px;font-size:20px;color:#444;width:380px;text-align:center}
.panel{top:140px;height:228px;background:var(--white);padding:18px}
.post{display:flex;gap:14px;margin-bottom:22px}
.post .thumb{width:72px;height:72px;flex:none;background:linear-gradient(135deg,#6d3a4a,#c06070)}
.post h4{font-family:"Raleway",Arial,sans-serif;font-size:14px;font-weight:600;color:var(--copper)}
.post p{margin-top:4px;font-size:10.5px;line-height:15px;color:var(--muted)}
.post small{display:block;margin-top:4px;font-size:9px;color:var(--copper)}
.team-top{display:flex;gap:14px}
.team-pic{width:140px;height:110px;flex:none;background:linear-gradient(180deg,#e8eef2,#b9c4cc)}
.team-top p,.team-text{font-size:10.5px;line-height:15px;color:var(--muted)}
.team-text{margin-top:12px}
.blog-team .btn{top:394px}

/* contact */
.contact{height:963px;background:var(--dark)}
.contact h2{top:48px;font-size:20px;color:var(--white)}
.contact .ornament{top:88px}
.clinics{left:212px;top:128px;width:776px;display:grid;grid-template-columns:1fr 1fr 1fr;text-align:center}
.clinic{padding:4px 10px;border-left:1px solid #5a5551}
.clinic:first-child{border-left:none}
.clinic h4{font-size:11px;font-weight:600;color:var(--copper)}
.clinic p{margin-top:4px;font-size:11.5px;line-height:17px;color:var(--white)}
.contact h3.form-title{top:244px;font-size:20px;color:var(--white)}
.appointment{left:324px;top:300px;width:556px}
.field-row{display:flex;gap:14px;margin-bottom:14px}
.field{flex:1;height:38px;border:1px solid #8a837d;padding:0 12px;line-height:36px;font-size:11px;color:#aaa;display:flex;justify-content:space-between;align-items:center}
.field svg{width:10px;height:10px}
.field.area{height:122px;align-items:flex-start}
.appointment .submit{display:block;width:100%;height:42px;line-height:42px;text-align:center;font-size:13px;margin-top:22px}

/* footer */
.footer-links{left:212px;top:756px;width:800px;display:grid;grid-template-columns:170px 150px 198px 155px 130px}
.footer-links h5{font-family:"Raleway",Arial,sans-serif;font-size:11px;font-weight:700;color:var(--white);text-transform:uppercase;margin-bottom:8px}
.footer-links li{list-style:none;font-size:10.5px;line-height:18px;color:#bbb}
.bottom-bar{height:61px;background:var(--footer)}
.bottom-bar .copy{left:212px;top:22px;font-size:10.5px;color:#aaa}
.social{right:212px;top:16px;display:flex;align-items:center;gap:6px;font-size:11px;color:#bbb}
.social span.dot{width:26px;height:26px;border-radius:50%;background:#555}
.social .label{margin-right:8px}
</style>
</head>
<body>

<header class="site-header">
  <div class="abs brand"><span class="brand-mark"></span><span class="brand-name">Harbourline Institute</span></div>
  <div class="abs request">Request a Consultation <b>(02) 5550 1290</b></div>
  <div class="abs header-btns"><span class="btn btn-copper">Make an appointment</span><span class="btn btn-dark">Contact us</span></div>
  <nav class="abs main-nav"><span class="active">Home</span><span>About us</span><span>Procedures</span><span>News</span><span>Patient resources</span><span>Contact us</span></nav>
</header>

<section class="hero">
  <div class="abs hero-photo" role="img" aria-label="Hero photograph of a smiling woman touching her cheek"></div>
  <div class="abs hero-copy">
    <h1>At the institute of<br>aesthetic plastic surgery</h1>
    <div class="hero-tag"><span class="line"></span>Your future looks beautiful<span class="line"></span></div>
    <svg class="play" viewBox="0 0 36 36"><circle cx="18" cy="18" r="18" fill="#2b2b2b"/><path d="M14 11 L26 18 L14 25 Z" fill="#fff"/></svg>
    <p>Watch our successful treatment<br>videos on our video channel</p>
    <span class="btn btn-copper">Schedule a consultation</span>
  </div>
</section>

<section class="welcome">
  <h2 class="abs center h-title">Welcome to Harbourline Institute of Plastic Surgery</h2>
  <svg class="ornament" viewBox="0 0 70 14"><line x1="0" y1="7" x2="26" y2="7" stroke="#d4a06a" stroke-width="2"/><line x1="44" y1="7" x2="70" y2="7" stroke="#d4a06a" stroke-width="2"/><rect x="30" y="2" width="10" height="10" transform="rotate(45 35 7)" fill="#d4a06a"/></svg>
  <div class="abs copy">
    <p>You can expect beautiful results at the Institute of Aesthetic Plastic Surgery. Offering a full range of face, breast and body enhancement, including facelifts, breast augmentation, lift, reduction and tummy tucks, we offer caring, natural results every day in your transformation journey.</p>
    <p>Dr Halverson is one of the region's most trusted specialists in plastic and cosmetic surgery, supported by a highly qualified, professional team. As a leading plastic surgery clinic, we use the most modern techniques to minimise scarring, helping you look better, feel better and enjoy a beautiful new you.</p>
  </div>
  <span class="abs btn btn-copper">Read more</span>
</section>

<section class="procedures">
  <h2 class="abs center h-title">We provide complete range of surgical and non-surgical proceedure</h2>
  <svg class="ornament" viewBox="0 0 70 14"><line x1="0" y1="7" x2="26" y2="7" stroke="#d4a06a" stroke-width="2"/><line x1="44" y1="7" x2="70" y2="7" stroke="#d4a06a" stroke-width="2"/><rect x="30" y="2" width="10" height="10" transform="rotate(45 35 7)" fill="#d4a06a"/></svg>
  <div class="abs proc-item" style="left:194px"><div class="proc-circle"><div role="img" aria-label="Face procedure photograph" style="background:radial-gradient(circle at 50% 40%,#f3dcc9,#d9b59a 70%)"></div></div><h3>Face Procedure</h3></div>
  <div class="abs proc-item" style="left:403px"><div class="proc-circle"><div role="img" aria-label="Breast procedure photograph" style="background:radial-gradient(circle at 50% 50%,#f1d7c5,#c99e82 75%)"></div></div><h3>Breast Procedure</h3></div>
  <div class="abs proc-item" style="left:612px"><div class="proc-circle"><div role="img" aria-label="Body procedure photograph" style="background:radial-gradient(circle at 50% 50%,#f0d2bb,#c08c6c 75%)"></div></div><h3>Body Procedure</h3></div>
  <div class="abs proc-item" style="left:824px"><div class="proc-circle"><div role="img" aria-label="Non surgical procedure photograph" style="background:radial-gradient(circle at 50% 45%,#f5e2d4,#dcc0ab 70%)"></div></div><h3>Non Surgical Procedure</h3></div>
  <div class="abs proc-btns"><span class="btn btn-copper">View all procedures</span><span class="btn btn-white">Make an appointment</span></div>
</section>

<section class="doctor">
  <div class="abs doctor-photo" role="img" aria-label="Portrait of the surgeon in shirt and tie"></div>
  <div class="abs doctor-copy">
    <h2>Meet Dr. Halverson (M.D. FRCSC)</h2>
    <p class="intro">Dr Halverson has remained the same from the day he elected to become a surgeon: to provide his patients with natural, beautiful results. Today, his thriving practice is testament to what he set out to achieve from the very beginning, changing a person's quality of life through self-improvement.</p>
    <h3>Professional affiliations</h3>
    <ul class="affil">
      <li><svg viewBox="0 0 12 12"><path d="M1 6 L4.5 9.5 L11 2" stroke="#d4a06a" stroke-width="2" fill="none"/></svg>Southern Society of Plastic Surgeons (SSPS)</li>
      <li><svg viewBox="0 0 12 12"><path d="M1 6 L4.5 9.5 L11 2" stroke="#d4a06a" stroke-width="2" fill="none"/></svg>Pacific Society of Aesthetic Surgeons (PSAS)</li>
      <li><svg viewBox="0 0 12 12"><path d="M1 6 L4.5 9.5 L11 2" stroke="#d4a06a" stroke-width="2" fill="none"/></svg>Global Aesthetic Surgery Council (GASC)</li>
      <li><svg viewBox="0 0 12 12"><path d="M1 6 L4.5 9.5 L11 2" stroke="#d4a06a" stroke-width="2" fill="none"/></svg>Fellow of the Coastal College of Surgeons (FCCS)</li>
      <li><svg viewBox="0 0 12 12"><path d="M1 6 L4.5 9.5 L11 2" stroke="#d4a06a" stroke-width="2" fill="none"/></svg>National Medical Guild (NMG)</li>
    </ul>
    <div class="doctor-btns"><span class="btn btn-copper">Tell me</span><span class="btn btn-white">Make an appointment</span></div>
  </div>
</section>

<section class="certified">
  <h2 class="abs h-title">Certified by</h2>
  <div class="abs badge" style="left:400px"></div>
  <div class="abs badge" style="left:558px"></div>
  <div class="abs badge square" style="left:720px"></div>
  <div class="abs badge" style="left:860px"></div>
</section>

<section class="features">
  <div class="abs feature-card" style="left:212px"><div class="pic" role="img" aria-label="Cool contouring treatment photograph" style="background:linear-gradient(135deg,#7fb3d8,#e7c5ad)"></div><h3>Cool Contouring</h3><p>Gentle non-surgical fat reduction that sculpts stubborn areas with no downtime.</p><span class="btn btn-copper">Learn more</span></div>
  <div class="abs feature-card" style="left:493px"><div class="pic" role="img" aria-label="Mommy makeover photograph" style="background:linear-gradient(135deg,#cfe1ee,#e9cdb8)"></div><h3>Mommy Makeover</h3><p>Restore your pre-pregnancy figure with a tailored blend of body procedures.</p><span class="btn btn-copper">Learn more</span></div>
  <div class="abs feature-card" style="left:774px"><div class="pic" role="img" aria-label="Anti-wrinkle injection photograph" style="background:linear-gradient(135deg,#6a8fb0,#e4c2a8)"></div><h3>Antiwrinkle Injections</h3><p>Soften fine lines and wrinkles for a refreshed, natural looking result.</p><span class="btn btn-copper">Learn more</span></div>
</section>

<section class="gallery">
  <h2 class="abs center h-title">Galleries before and after proceedure</h2>
  <svg class="ornament" viewBox="0 0 70 14"><line x1="0" y1="7" x2="26" y2="7" stroke="#d4a06a" stroke-width="2"/><line x1="44" y1="7" x2="70" y2="7" stroke="#d4a06a" stroke-width="2"/><rect x="30" y="2" width="10" height="10" transform="rotate(45 35 7)" fill="#d4a06a"/></svg>
  <div class="abs tabs"><span class="on">FACE</span><span>BREAST</span><span>BODY</span><span>NON SURGICAL</span></div>
  <div class="abs tab-rule"></div>
  <div class="abs gallery-photo"><div role="img" aria-label="Before and after face result photograph"></div></div>
  <div class="abs gallery-copy">
    <h3>FACE</h3>
    <p>Our face gallery shows real patient results from facelift, eyelid and nose surgery. Each case is photographed before treatment and again after healing, so you can judge natural outcomes. Browse the cases to see what may be possible for you.</p>
    <div class="hint">Click on Procedure below to see before and after photos</div>
    <ul class="g-list"><li>Facelift</li><li>Browlift</li><li>Rhinoplasty</li><li>Otoplasty</li><li>Blepharoplasty</li></ul>
    <div class="gallery-btns"><span class="btn btn-copper">View all photos</span><span class="btn btn-white">Talk to Dr. Halverson</span></div>
  </div>
</section>

<section class="blog-team">
  <h2 class="abs h-title" style="left:204px">Latest blog posts</h2>
  <h2 class="abs h-title" style="left:694px">Our team</h2>
  <div class="abs panel" style="left:212px;width:379px">
    <div class="post"><div class="thumb" role="img" aria-label="Blog post photograph"></div><div><h4>New york party 2015</h4><p>Highlights from our patient evening, with talks on recovery and results.</p><small>26.12.2015</small></div></div>
    <div class="post"><div class="thumb" role="img" aria-label="Blog post photograph"></div><div><h4>New york party 2015</h4><p>Meet the team and learn about our newest surgical techniques this year.</p><small>26.12.2015</small></div></div>
  </div>
  <div class="abs panel" style="left:621px;width:367px">
    <div class="team-top"><div class="team-pic" role="img" aria-label="Group photograph of the clinic team"></div><p>Our caring team of nurses, coordinators and surgeons support you from your first consultation through recovery, answering every question along the way.</p></div>
    <p class="team-text">Every member of our staff is trained to the highest standard, so you feel safe, informed and comfortable at each step.</p>
  </div>
  <span class="abs btn btn-copper" style="left:443px">See all posts</span>
  <span class="abs btn btn-copper" style="left:864px">Meet our team</span>
</section>

<section class="contact">
  <h2 class="abs center h-title">Contact or reach to our clinics</h2>
  <svg class="ornament" viewBox="0 0 70 14"><line x1="0" y1="7" x2="26" y2="7" stroke="#d4a06a" stroke-width="2"/><line x1="44" y1="7" x2="70" y2="7" stroke="#d4a06a" stroke-width="2"/><rect x="30" y="2" width="10" height="10" transform="rotate(45 35 7)" fill="#d4a06a"/></svg>
  <div class="abs clinics">
    <div class="clinic"><h4>Northcliff</h4><p>412 Seaview Rd, Suite 12<br>Northcliff, NSW 2999</p></div>
    <div class="clinic"><h4>Ashgrove</h4><p>Level 1, 77 Fenwick Street<br>2998</p></div>
    <div class="clinic"><h4>Riverton</h4><p>Tel 02 5550 1720<br>3/9 Calder St, Riverton, NSW 2997</p></div>
  </div>
  <h3 class="abs center h-title form-title">Make an appointment</h3>
  <div class="abs appointment">
    <div class="field-row"><div class="field">First Name</div><div class="field">Last Name</div></div>
    <div class="field-row"><div class="field">Phone Number</div><div class="field">Email Address</div></div>
    <div class="field-row"><div class="field">Select Date<svg viewBox="0 0 10 10"><path d="M1 3 L5 7 L9 3" stroke="#aaa" fill="none"/></svg></div><div class="field">Select Time<svg viewBox="0 0 10 10"><path d="M1 3 L5 7 L9 3" stroke="#aaa" fill="none"/></svg></div></div>
    <div class="field-row"><div class="field area">Type your message here...</div></div>
    <span class="btn btn-copper submit">Talk to Dr. Halverson</span>
  </div>
  <div class="abs footer-links">
    <div><h5>Quick links</h5><ul><li>Home</li><li>About Us</li><li>News</li><li>Patient Resources</li><li>Contact Us</li><li>Make an Appointment</li></ul></div>
    <div><h5>Face</h5><ul><li>Facelift</li><li>Rhinoplasty</li><li>Blepharoplasty</li><li>Browlift</li><li>Otoplasty</li></ul></div>
    <div><h5>Breast</h5><ul><li>Breast Augmentation</li><li>Breast Reduction</li><li>Breast Lift with Implants</li><li>Breast Reduction</li><li>Gynaecomastia</li><li>Mommy Makeover</li></ul></div>
    <div><h5>Body</h5><ul><li>Tummy Tuck</li><li>Liposuction</li><li>Labiaplasty</li><li>Brazilian Butt Lift</li><li>Mummy Makeover</li></ul></div>
    <div><h5>Non surgical</h5><ul><li>Anti Wrinkle</li><li>Dermal Fillers</li><li>Cool Contouring</li><li>Fillers</li><li>Skin Peels</li></ul></div>
  </div>
</section>

<footer class="bottom-bar">
  <div class="abs copy">© Copyright Harbourline Institute of Aesthetic Plastic Surgery. All Rights Reserved.</div>
  <div class="abs social"><span class="label">We're Social</span><span class="dot"></span><span class="dot"></span><span class="dot"></span><span class="dot"></span></div>
</footer>

</body>
</html>
```